BrightFern Life Insurance Web Design Project

We need a beautiful and simple website design to better explain our life insurance business, products and why people need life insurance.
We want the site to stand out as being simple and compelling.
As we are an old "friendly society" that has been in Australia for 130 years, we want to stand for trust, simplicity, but also longevity and security (we are supported by a global reinsurer)
We will allow customers to directly get a quote and apply for life insurance through the website.
We want a very modern look, with our exisiting gold and dark blue colours.
Target Market(s)
30-50 YOs
Industry/Entity Type
Life Insurance
Requirements
Must have
- - Life insurance quick quotation tool.
- Phone number.
- Ability to drill to information on different types of life insurance.
- Positive imagery
- our logo (refer www.brightfern-example.com.au)
Nice to have
- Target market is 30-40year olds.
Portal for advisers to access
Should not have
- Clip art
Cliched images

```html
<!DOCTYPE html>
<html lang="en">
<head>
<meta charset="utf-8">
<title>BrightFern Life Insurance</title>
<link rel="stylesheet" href="https://fonts.googleapis.com/css2?family=Open+Sans:ital,wght@0,400;0,600;0,700;1,400&family=Noto+Serif:ital@0;1&family=Quicksand:wght@300&display=swap">
<style>
:root{
  --brand:#3a2d86;
  --gold:#d4b02a;
  --nav-grey:#d3d8d8;
  --panel:#dde9ea;
  --field:#b9b9b9;
  --text:#2c2c2c;
  --footer:#333333;
  --muted-white:#f4f8f8;
}
*{box-sizing:border-box;margin:0;padding:0}
html,body{width:1200px;height:1184px;overflow:hidden;background:#fff}
body{position:relative;font-family:"Open Sans",Arial,sans-serif;color:var(--text)}
.abs{position:absolute}
.call-btn{left:862px;top:33px;width:206px;height:52px;background:linear-gradient(#d6dcdc,#c3cbcb);border-radius:3px;box-shadow:0 2px 3px rgba(0,0,0,.35);color:#fff;text-align:center;font-weight:600}
.call-btn .small{display:block;font-size:15px;margin-top:5px}
.call-btn .tel{display:block;font-size:17px;margin-top:1px}
.brand{left:128px;top:110px;display:flex;align-items:center;gap:12px}
.brand .mark{width:38px;height:38px;background:var(--brand)}
.brand .name{font-size:29px;font-weight:400;color:var(--brand)}
.main-nav{left:367px;top:137px;width:700px;height:37px;background:var(--nav-grey)}
.main-nav a{position:absolute;top:9px;font-size:15px;font-weight:700;color:#fff;text-decoration:none}
.main-nav a.active{color:var(--brand)}
.hero{left:127px;top:174px;width:940px;height:331px;background:linear-gradient(180deg,#9fb6c8 0%,#b6c6cf 58%,#8ea1a8 66%,#a9a49a 82%,#8f8a82 100%)}
.hero-title{left:153px;top:278px;font-family:"Quicksand",sans-serif;font-weight:300;font-size:38px;line-height:44px;color:#fff}
.btn{display:block;background:var(--brand);color:#fff;font-weight:600;text-align:center;border-radius:4px;text-decoration:none}
.hero-btn{left:152px;top:375px;width:159px;height:36px;line-height:36px;font-size:17px}
.dots{left:579px;top:517px;display:flex;gap:6px}
.dots span{width:8px;height:8px;border-radius:50%;background:#333}
.dots span.on{background:#fff;border:2px solid #555}
.section-title{font-family:"Noto Serif",serif;font-size:18px;color:#333}
.rule{height:6px;background:var(--nav-grey)}
.shortcuts-title{left:130px;top:564px}
.shortcuts-rule{left:127px;top:590px;width:220px}
.shortcuts{left:127px;top:603px;list-style:none;font-size:15px;line-height:18px}
.shortcuts li{position:relative;padding-left:11px;margin-bottom:10px}
.shortcuts li::before{content:"";position:absolute;left:0;top:6px;width:6px;height:6px;background:#333}
.intro-title{left:446px;top:564px;font-style:italic}
.intro-rule{left:446px;top:590px;width:620px}
.intro-text{left:448px;top:603px;width:610px;font-size:15px;line-height:18px}
.intro-text p{margin-bottom:18px}
.sm-btn{width:120px;height:24px;line-height:23px;font-size:15px}
.intro-btn{left:449px;top:712px}
.info-panel{left:127px;top:781px;width:940px;height:292px;background:var(--panel)}
.col-title{top:795px;display:flex;align-items:center;gap:5px}
.col-title::before{content:"";width:12px;height:12px;border-radius:50%;background:#fff}
.col-text{top:840px;font-size:16px;line-height:18px;width:280px}
.soft{color:var(--muted-white);font-style:italic;font-size:15px}
.testimonial{left:447px;top:938px;width:290px;font-family:Arial,sans-serif;font-size:11px;line-height:12px;color:#5aa9a6}
.field{left:767px;width:294px;background:var(--field);color:#fff;font-weight:600;font-size:14px;padding:7px 10px}
.footer{left:0;top:1108px;width:1200px;height:76px;background:var(--footer);color:#fff}
.footer-nav{left:155px;top:1114px;display:flex;font-family:"Noto Serif",serif;font-size:17px}
.footer-nav a{color:#fff;text-decoration:none;padding:0 11px;border-left:2px solid var(--gold);line-height:26px}
.footer-nav a:first-child{border-left:0;padding-left:0}
.footer-note{left:151px;top:1156px;font-size:15px}
.social{left:938px;top:1142px;display:flex;gap:15px}
.social span{width:34px;height:34px;border-radius:50%;background:#bbbbbb}
</style>
</head>
<body>
<div class="abs call-btn"><span class="small">Call us now!</span><span class="tel">Tel: 1300 000 123</span></div>

<div class="abs brand"><span class="mark"></span><span class="name">BrightFern</span></div>

<nav class="abs main-nav">
  <a class="active" href="#" style="left:11px">Home</a>
  <a href="#" style="left:117px">Choosing Life Insurance</a>
  <a href="#" style="left:353px">Get Life Insurance</a>
  <a href="#" style="left:532px">Claims</a>
  <a href="#" style="left:618px">About Us</a>
</nav>

<div class="abs hero" role="img" aria-label="Photo of a family of four walking hand in hand along a beach"></div>
<h1 class="abs hero-title" style="font-weight:300">Your partner<br>for life</h1>
<a class="abs btn hero-btn" href="#">Get a Quate</a>
<div class="abs dots"><span class="on"></span><span></span><span></span><span></span></div>

<h2 class="abs section-title shortcuts-title" style="font-weight:400">Insurance Shortcuts</h2>
<div class="abs rule shortcuts-rule"></div>
<ul class="abs shortcuts">
  <li>Life Insurance</li>
  <li>Total and permanent<br>disablement insurance</li>
  <li>Trauma insurance</li>
  <li>Income protection insurance</li>
  <li>Business expenses insurance</li>
</ul>

<h2 class="abs section-title intro-title" style="font-weight:400">Get LIfe Insurance</h2>
<div class="abs rule intro-rule"></div>
<div class="abs intro-text">
  <p>It is an important moment when you appreciate the value of the things in your life that really matter.</p>
  <p>Now that you have decided to get life insurance, BrightFern makes the process simple and straightforward.</p>
</div>
<a class="abs btn sm-btn intro-btn" href="#">Learn more</a>

<div class="abs info-panel"></div>
<h3 class="abs section-title col-title" style="left:136px;font-weight:400">Latest News</h3>
<div class="abs col-text" style="left:136px">Share offer announced BrightFern has announced a non-renounceable pro rata offer of Shares each at an issue price of $0.50 to eligible shareholders on the basis of eight shares for every seven shares on 15th July 2011.
  <p class="soft" style="margin-top:16px">Sign up here to receive regular e-newsletter.</p>
</div>
<a class="abs btn sm-btn" href="#" style="left:134px;top:1027px">Learn more</a>

<h3 class="abs section-title col-title" style="left:446px;font-weight:400">Why choose BrightFern</h3>
<div class="abs col-text" style="left:446px">BrightFern Life Limited has more than 130 years experience as one of Australia's leading friendly societies
  <p class="soft" style="margin-top:14px">Testimonials</p>
</div>
<p class="abs testimonial">Lorem Ipsum is simply dummy text of the printing and typesetting industry. Lorem Ipsum has been the industry's standard dummy text ever since the 1500s, when an unknown printer took a galley of type and scrambled it to make a type specimen book</p>
<p class="abs soft" style="left:675px;top:1002px">Clara D.</p>
<a class="abs btn sm-btn" href="#" style="left:447px;top:1027px">Learn more</a>

<h3 class="abs section-title col-title" style="left:767px;font-weight:400">Contact an advicer</h3>
<div class="abs field" style="top:844px;height:35px">Email</div>
<div class="abs field" style="top:889px;height:35px">Tel</div>
<div class="abs field" style="top:934px;height:79px;padding-top:3px">Contect</div>
<a class="abs btn sm-btn" href="#" style="left:767px;top:1027px">Submit</a>

<footer class="abs footer"></footer>
<nav class="abs footer-nav">
  <a href="#">Home</a><a href="#">Choosing Life Insurance</a><a href="#">Get Life Insurance</a><a href="#">Claims</a><a href="#">About Us</a><a href="#">Terms of Use and Privacy Policy</a>
</nav>
<p class="abs footer-note" style="color:#fff">Call us now on 1300 000 123 or send us an email today</p>
<div class="abs social" aria-label="Social links"><span></span><span></span><span></span></div>
</body>
</html>
```